Neurofeedback Specialist and Sober Living Advocate and Administrator needs a logo design

I need a logo design to capture/demonstrate my work and life's mission:
I provide neurofeedback training services to people from all walks of life, especially for people in recovery from addiction and substance abuse. I am also the administrator for a beautiful sober living home on the beach in Malibu, CA .
Neurofeedback is a brain training exercise that takes advantage of the brain's ability to heal itself, and it speeds up the brain's regeneration process after it has undergone some kind of stress (such as surviving a traumatic brain injury, substance abuse, recovery from mental illness, etc.) I provide neurofeedback sessions privately and at several mental health and substance abuse recovery centers in Malibu and the surrounding areas. I also train other practitioners on how to become neurofeedback providers. I work with adults and children, all ages, with all capability levels, and with a range of needs: from Autism to Peak Performance... Neurofeedback training has been known to decrease anxiety, improve sleep, alleviate symptoms of trauma/PTSD, eliminate symptoms of depression such as fatigue, sadness, motivation issues, improve focus, it can reduce the intensity of chronic pain, help eliminate migraines and seizures, and more. I also provide Neurofeedback to maximize peak performance and am typically the go-to neuroveedback speaiclist in the Malibu, CA area for celebrities such as sports heroes, performers (acting and music), CEO's, etc. I have a new website, brainwavecoveline.com (a work in progress) which features some of the colors I like (such as blue and green) but I also like most other colors except for orange and brown colors, those shades would be the two that I would typically reject.
As the administrator for the sober living home, I help clients get and stay sober as they transition back into their lives... I help guide our clients back into "the real world" after they have completed at least 30 days of treatment at an inpatient rehab or mental health facility. Our sober living website is ClearHarborHouseAtShore.com, the colors are blue and white, and our sober living home is considered a boutique business, as we provide personal attention and care, and we can host no more than 10 clients at a time.
Maybe on one side of the card you could have the Neurofeedback Specialist info and on the other side you could have the Sober Living Advocate and Administrator info...

```html
<!DOCTYPE html>
<html lang="en">
<head>
<meta charset="utf-8">
<title>Business Cards – Clear Harbor House &amp; Brainwave Cove</title>
<link href="https://fonts.googleapis.com/css2?family=Open+Sans:wght@400;600&display=swap" rel="stylesheet">
<style>
  :root {
    --backdrop: #cfcfcf;
    --card: #f4f4f2;
    --ink: #1d1d1d;
    --harbor-blue: #2b86b8;
    --cove-teal: #7fc4c4;
    --icon-teal: #6fb7b3;
  }
  * { box-sizing: border-box; margin: 0; padding: 0; }
  html, body { width: 1200px; height: 900px; overflow: hidden; }
  body {
    background: radial-gradient(circle at 50% 45%, #ececec 0%, var(--backdrop) 75%);
    font-family: "Open Sans", Arial, sans-serif;
    color: var(--ink);
    position: relative;
  }
  .card {
    position: absolute;
    width: 560px;
    height: 320px;
    background: var(--card);
    border-radius: 22px;
    box-shadow: 0 10px 24px rgba(0,0,0,0.25);
  }
  .card-front { left: 90px; top: 100px; }
  .card-back { left: 550px; top: 470px; }

  /* Front: sober living home */
  .home-brand {
    position: absolute;
    left: 0; right: 0; top: 108px;
    display: flex; align-items: center; justify-content: center; gap: 14px;
  }
  .brand-dot {
    width: 34px; height: 34px; border-radius: 50%;
    border: 4px solid var(--harbor-blue);
  }
  .home-name {
    font-size: 38px; font-weight: 600; letter-spacing: -0.5px;
    color: var(--ink);
  }
  .home-phone {
    position: absolute; left: 0; right: 0; top: 222px;
    display: flex; align-items: center; justify-content: center; gap: 8px;
    font-size: 14px;
  }
  .home-phone svg { fill: var(--harbor-blue); }

  /* Back: neurofeedback practice */
  .practice-brand {
    position: absolute; left: 38px; bottom: 60px;
    display: flex; align-items: center; gap: 10px;
  }
  .practice-dot {
    width: 44px; height: 44px; border-radius: 50%;
    background: var(--cove-teal);
  }
  .practice-name { font-size: 18px; font-weight: 400; letter-spacing: 0.5px; }

  .contact {
    position: absolute; left: 300px; top: 58px;
  }
  .contact-name { font-size: 22px; font-weight: 600; line-height: 1.1; }
  .contact-title { font-size: 14px; color: var(--cove-teal); margin-bottom: 12px; }
  .contact-line {
    display: flex; align-items: center; gap: 8px;
    font-size: 12.5px; line-height: 1.9;
  }
  .contact-line svg { flex: none; fill: var(--icon-teal); }
  .contact-address { font-size: 12.5px; line-height: 1.5; margin-top: 6px; padding-left: 22px; }
</style>
</head>
<body>

  <section class="card card-front" aria-label="Clear Harbor House card">
    <div class="home-brand">
      <span class="brand-dot"></span>
      <span class="home-name">Clear Harbor House</span>
    </div>
    <p class="home-phone">
      <svg width="14" height="12" viewBox="0 0 14 12" aria-hidden="true"><path d="M1 4 Q7 -1 13 4 L11 6 L9 4.5 L9 3 Q7 2.3 5 3 L5 4.5 L3 6 Z M3 7 H11 V11 H3 Z"/></svg>
      555.014.2210 or 555.014.2214
    </p>
  </section>

  <section class="card card-back" aria-label="Brainwave Cove card">
    <div class="practice-brand">
      <span class="practice-dot"></span>
      <span class="practice-name">BRAINWAVE COVE</span>
    </div>
    <div class="contact">
      <h1 class="contact-name">Marisol Trent</h1>
      <p class="contact-title">Neurofeedback Specialist</p>
      <p class="contact-line">
        <svg width="14" height="12" viewBox="0 0 14 12" aria-hidden="true"><path d="M1 4 Q7 -1 13 4 L11 6 L9 4.5 L9 3 Q7 2.3 5 3 L5 4.5 L3 6 Z M3 7 H11 V11 H3 Z"/></svg>
        555-014-2214
      </p>
      <p class="contact-line">
        <svg width="14" height="10" viewBox="0 0 14 10" aria-hidden="true"><path d="M0 0 H14 V10 H0 Z M1 1 L7 6 L13 1 Z" fill-rule="evenodd"/></svg>
        brainwavecoveline@mailbox.com
      </p>
      <p class="contact-line">
        <svg width="14" height="14" viewBox="0 0 14 14" aria-hidden="true"><circle cx="7" cy="7" r="6" fill="none" stroke="#6fb7b3" stroke-width="1.2"/><path d="M1 7 H13 M7 1 Q3 7 7 13 Q11 7 7 1" fill="none" stroke="#6fb7b3" stroke-width="1"/></svg>
        www.brainwavecoveline.com
      </p>
      <p class="contact-address">4410 Shoreline Drive<br>Cove Point, CA 90000</p>
    </div>
  </section>

</body>
</html>
```